Need a business card for our overland brand!

We had the logo made and we need a great design for our business card. Use the logo provide or tweak it however you see fit.

Contact Information for Business Card

Name, Title, Telephone, email, website

```html
<!DOCTYPE html>
<html lang="en">
<head>
<meta charset="utf-8">
<title>Ridgeway Trails – Business Card</title>
<link href="https://fonts.googleapis.com/css2?family=Montserrat:wght@400;700&display=swap" rel="stylesheet">
<style>
  :root {
    --stage: #e2e1de;
    --card: #ffffff;
    --accent: #1f9ec4;
    --navy: #243a54;
    --ink: #2a2a2a;
  }
  * { box-sizing: border-box; margin: 0; padding: 0; }
  html, body { width: 1200px; height: 801px; overflow: hidden; }
  body {
    background: var(--stage);
    font-family: "Montserrat", sans-serif;
    display: flex;
    align-items: center;
    justify-content: center;
    gap: 50px;
  }
  .card {
    position: relative;
    width: 525px;
    height: 300px;
    background: var(--card);
    border-radius: 16px;
    border-bottom: 4px solid var(--accent);
    box-shadow: 0 12px 30px rgba(0,0,0,0.18);
    overflow: hidden;
  }
  .card-front .accent-bar {
    position: absolute;
    top: 0; right: 36px;
    width: 14px; height: 54px;
    background: var(--accent);
  }
  .person {
    position: absolute;
    top: 22px; right: 62px;
    text-align: right;
  }
  .person-name {
    color: var(--accent);
    font-weight: 700;
    font-size: 22px;
    letter-spacing: 1px;
  }
  .person-title {
    color: var(--ink);
    font-size: 13px;
    margin-top: 2px;
  }
  .brand-small {
    position: absolute;
    left: 32px; top: 92px;
    display: flex; align-items: center; gap: 8px;
    color: var(--navy);
    font-weight: 700;
    font-size: 20px;
    line-height: 1.05;
    text-transform: uppercase;
  }
  .brand-mark { width: 12px; height: 12px; background: var(--accent); }
  .address {
    position: absolute;
    left: 32px; top: 160px;
    color: var(--ink);
    font-size: 12px;
    line-height: 1.45;
  }
  .contacts {
    position: absolute;
    left: 32px; top: 208px;
    list-style: none;
    color: var(--ink);
    font-size: 12px;
    line-height: 1.75;
  }
  .contacts li { display: flex; align-items: center; gap: 8px; }
  .contacts svg { width: 12px; height: 12px; fill: var(--accent); flex: none; }
  .card-back { display: flex; align-items: center; justify-content: center; }
  .brand-large {
    color: var(--navy);
    font-weight: 700;
    font-size: 62px;
    line-height: 0.95;
    text-transform: uppercase;
    text-align: center;
    letter-spacing: 1px;
  }
</style>
</head>
<body>
  <section class="card card-front">
    <div class="accent-bar"></div>
    <div class="person">
      <div class="person-name">DANIEL HART</div>
      <div class="person-title">Managing Director</div>
    </div>
    <div class="brand-small"><span class="brand-mark"></span><span>Ridgeway<br>Trails</span></div>
    <p class="address">Your address, City<br>State, Zip 1234</p>
    <ul class="contacts">
      <li><svg viewBox="0 0 24 24"><path d="M6.6 10.8a15 15 0 0 0 6.6 6.6l2.2-2.2a1 1 0 0 1 1-.25 11.4 11.4 0 0 0 3.6.57 1 1 0 0 1 1 1V20a1 1 0 0 1-1 1A17 17 0 0 1 3 4a1 1 0 0 1 1-1h3.5a1 1 0 0 1 1 1c0 1.25.2 2.45.57 3.57a1 1 0 0 1-.25 1z"/></svg>123 456 789</li>
      <li><svg viewBox="0 0 24 24"><path d="M2 5h20v14H2z M4 7v.5l8 5 8-5V7z" fill-rule="evenodd"/></svg>info@ridgewaytrails.com</li>
      <li><svg viewBox="0 0 24 24"><circle cx="12" cy="12" r="10"/></svg>www.ridgewaytrails.com</li>
    </ul>
  </section>
  <section class="card card-back">
    <div class="brand-large">Ridgeway<br>Trails</div>
  </section>
</body>
</html>
```